Tavern Business Card

I need a nice and sleek business card.

I need it to promote our website, our ratebook page, and or picthread page

Picthread would be: @marlowjoinery
website would be: www.marlowjoinery.example
ratebook would be: Marlow Joinery Inc (logo is fine)

Here are a list of service we offer.
1. Custom Kitchen Remodeling
2. Custom Bathroom Remodeling
3. Custom Closet Remodeling
4. Custom Bedroom Remodeling
5. Custom Bars
6. Custom Bookcases
7. Custom Staircases
8. Custom Ceilings

Please use the wording "Grain & Gable"
We also have been in business since 1992
and we have been serving the rich and famous since.

We do all types of designs, modern and renaissance.

Industry/Entity Type

Business

Contact Information for Business Card

Marlow Joinery, Inc.
58710 Bellamy Rd,. Unit 304-305
Dunmere, CA. 90999
Teodor Kell Varinsky - CEO
555-430-6628
marlowjoinery@postbox.example

```html
<!DOCTYPE html>
<html lang="en">
<head>
<meta charset="utf-8">
<title>Marlow Joinery Inc – Business Card</title>
<link rel="stylesheet" href="https://fonts.googleapis.com/css2?family=Crimson+Pro:wght@400;600;700&display=swap">
<style>
  :root {
    --page-bg: #232325;
    --card-bg: #2a1b13;
    --frame: #8c7c6b;
    --ink: #f1ebe2;
    --ink-soft: #ddd3c6;
    --mark: #b3a28a;
  }
  * { box-sizing: border-box; margin: 0; padding: 0; }
  html, body {
    width: 1200px; height: 1200px; overflow: hidden;
    background: var(--page-bg);
    font-family: "Crimson Pro", Georgia, serif;
    color: var(--ink);
  }
  .canvas { position: relative; width: 1200px; height: 1200px; }
  .card {
    position: absolute; left: 170px; width: 860px; height: 491px;
    background: var(--card-bg);
    box-shadow: 0 6px 24px rgba(0,0,0,.45);
  }
  .card--front { top: 79px; }
  .card--back { top: 630px; }

  .frame { position: absolute; inset: 22px; border: 1px solid var(--frame); }
  .frame::after { content: ""; position: absolute; inset: 5px; border: 1px solid var(--frame); }

  .brand { position: absolute; left: 60px; top: 120px; width: 300px; text-align: center; }
  .brand-mark { display: block; margin: 0 auto 14px; }
  .brand-name {
    font-size: 13px; letter-spacing: .28em; text-transform: uppercase; color: var(--ink-soft);
  }
  .address { margin-top: 18px; font-size: 20px; line-height: 1.25; color: var(--ink); }

  .contact { position: absolute; left: 465px; top: 72px; width: 300px; }
  .person-name { font-size: 29px; font-weight: 700; line-height: 1.1; }
  .person-role { font-size: 16px; margin-top: 6px; color: var(--ink-soft); }
  .rule { height: 1px; background: var(--frame); margin: 12px 0 14px; }
  .detail { display: flex; font-size: 17px; line-height: 1.3; }
  .detail dt { font-weight: 700; width: 66px; flex: none; }
  .detail dd { color: var(--ink-soft); }
  .social { margin-top: 26px; }
  .social .detail dt { width: 96px; }

  .tagline {
    position: absolute; left: 0; right: 0; bottom: 44px; text-align: center;
    font-size: 16px; letter-spacing: .2em; color: var(--ink-soft);
  }

  .back-brand { position: absolute; left: 0; right: 0; top: 92px; text-align: center; }
  .back-brand .brand-mark { margin-bottom: 26px; }
  .back-brand .brand-name { font-size: 20px; letter-spacing: .3em; color: var(--ink); }
  .since { margin-top: 28px; font-size: 17px; letter-spacing: .3em; color: var(--ink-soft); }
</style>
</head>
<body>
<main class="canvas">

  <section class="card card--front" aria-label="Business card front">
    <div class="frame"></div>

    <div class="brand">
      <svg class="brand-mark" width="70" height="70" viewBox="0 0 70 70" aria-hidden="true">
        <circle cx="35" cy="35" r="33" fill="none" stroke="var(--mark)" stroke-width="1.5"/>
      </svg>
      <p class="brand-name">Marlow Joinery Inc.</p>
      <p class="address">58710 Bellamy Rd<br>Unit 304 305 Dunmere<br>CA. 90999</p>
    </div>

    <div class="contact">
      <h1 class="person-name">Teodor Kell Varinsky</h1>
      <p class="person-role">CEO</p>
      <div class="rule"></div>
      <dl>
        <div class="detail"><dt>Phone</dt><dd>555 - 430 - 6628</dd></div>
        <div class="detail"><dt>Email</dt><dd>marlowjoinery@postbox.example</dd></div>
      </dl>
      <div class="rule"></div>
      <dl class="social">
        <div class="detail"><dt>Picthread</dt><dd>@marlowjoinery</dd></div>
        <div class="detail"><dt>Web</dt><dd>www.marlowjoinery.example</dd></div>
        <div class="detail"><dt>Ratebook</dt><dd>Marlow Joinery Inc</dd></div>
      </dl>
    </div>

    <p class="tagline">-Grain &amp; Gable-</p>
  </section>

  <section class="card card--back" aria-label="Business card back">
    <div class="back-brand">
      <svg class="brand-mark" width="130" height="130" viewBox="0 0 130 130" aria-hidden="true">
        <circle cx="65" cy="65" r="63" fill="none" stroke="var(--mark)" stroke-width="2"/>
      </svg>
      <p class="brand-name">Marlow Joinery Inc.</p>
      <p class="since">- Since 1992 -</p>
    </div>
  </section>

</main>
</body>
</html>
```